依頼詳細
構成は添付ファイルのとおりです。
ロゴはサイト名の公開ができないためとりあえず Pelvo Mirant でデザインをお願いいたします。
後日正式なものと入れ替えていただきますが、その際に多少調整をお願いする予定です。
サイトURL
ページ数
3ページ
希望イメージ
シンプル 複雑
単色 カラフル
暗い 明るい
日常 高級
遊び心 厳粛
未来的 伝統的
女性的 男性的
希望する色
青系、水色系
納品ファイル
• 高解像度JPG (.jpg)
補足説明
XDファイルでもOKです。
少々分かりづらい部分がありましたので追記です。

・右上トップメニューは例えばハンバーガーアイコンのようなものになるかと思います。
出会い掲示板以外のメニュー(チャットやコミュニティリンク集などへ移動できます)

・タイトル下部に投稿内容のプレビュー(1-2行程度)を表示願います。

・写真は添付がある投稿とない投稿があるため、ない場合においては写真の部分の余白を埋めてください。

・ページ2
プロフィール・ラベル・キーワード  3つのタブに別れた状態
と記載のある部分ですがPowerPointの資料においては「プロフィール」のタブが選択された状態を示しています
上部で3分割されて個々の検索条件をしていする作りですがコンペにおいては「プロフィール」タブが選択された状態にしておいてください。

「絞り込み検索結果の条件表示」の部分に指定した条件が表示され、どういう状態で抽出しているかが分かる仕組みです。

よろしくお願いいたします。
■ 選んだ理由

いろいろ悩みましたがこちらに決定させて頂きました。

■ 提案者全員のお礼・コメント

多くのご提案ありがとうございます!

```html
<!DOCTYPE html>
<html lang="ja">
<head>
<meta charset="utf-8">
<title>出会い掲示板</title>
<link rel="stylesheet" href="https://fonts.googleapis.com/css2?family=Noto+Sans+JP:wght@400;500;700&family=Noto+Serif+JP:wght@500&display=swap">
<style>
:root{
  --page:#2b4a86;
  --header:#c3e6f6;
  --ink:#172a4f;
  --white:#ffffff;
  --heart:#e8623f;
  --status:#b9c2cc;
  --nav:#ffffff;
  --nav-icon:#1a2238;
}
*{margin:0;padding:0;box-sizing:border-box}
html,body{width:1200px;height:2596px;overflow:hidden}
body{background:var(--page);font-family:"Noto Sans JP",sans-serif;color:var(--white);position:relative}
.status-bar{position:absolute;top:0;left:0;width:1200px;height:60px;background:#f3f5f7}
.status-bar .dots{position:absolute;right:28px;top:18px;display:flex;gap:14px}
.status-bar .dots span{width:22px;height:22px;border-radius:50%;background:var(--status)}
.board-header{position:absolute;top:0;left:0;width:1200px;height:600px;background:var(--header);border-radius:0 0 0 130px;padding-top:0}
.board-header .menu{position:absolute;left:70px;top:148px;width:68px}
.board-header .menu span{display:block;height:7px;background:var(--ink);margin-bottom:13px}
.board-title{position:absolute;left:180px;top:120px;font-size:62px;font-weight:700;color:var(--ink);letter-spacing:1px}
.filter-list{position:absolute;left:180px;top:250px;list-style:none;font-size:52px;line-height:88px;color:var(--ink)}
.favorite{position:absolute;left:925px;top:92px;width:246px;height:222px}
.post{position:absolute;left:48px;width:1110px;height:600px}
.post-title{font-size:64px;font-weight:700;line-height:80px;letter-spacing:1px}
.post-photo{position:absolute;left:0;top:96px;width:416px;height:416px;border-radius:28px;background:linear-gradient(160deg,#d9c6a8 0%,#a8885e 45%,#6c5540 100%)}
.post-body{position:absolute;left:492px;top:112px;width:612px}
.post-tag{font-size:54px;font-weight:700;line-height:70px}
.post-name{font-size:70px;font-weight:500;line-height:96px;margin-top:14px}
.post-preview{font-size:44px;line-height:60px;margin-top:10px;white-space:nowrap;overflow:hidden;text-overflow:ellipsis}
.post-meta{position:absolute;left:0;top:514px;width:1110px;display:flex;justify-content:space-between;font-family:"Noto Serif JP",serif;font-size:44px;font-weight:500;line-height:60px}
.bottom-nav{position:absolute;left:0;top:2450px;width:1200px;height:146px;background:var(--nav);display:flex;justify-content:space-around;align-items:center;padding:0 110px}
.bottom-nav svg{width:120px;height:100px}
</style>
</head>
<body>
<div class="board-header">
  <div class="menu" aria-label="メニュー"><span></span><span></span><span></span></div>
  <h1 class="board-title">[東京都]出会い掲示板</h1>
  <ul class="filter-list">
    <li>プロフ：10代/20代</li>
    <li>ラベル：グラマー･スレンダー</li>
    <li>キーワード：新宿</li>
  </ul>
  <svg class="favorite" viewBox="0 0 246 222" aria-label="お気に入り"><path fill="var(--heart)" d="M123 222 C60 170 0 120 0 66 C0 28 30 0 66 0 C92 0 112 14 123 34 C134 14 154 0 180 0 C216 0 246 28 246 66 C246 120 186 170 123 222Z"/></svg>
</div>
<div class="status-bar"><div class="dots"><span></span><span></span><span></span></div></div>

<article class="post" style="top:570px">
  <h2 class="post-title">今から新宿で会いませんか?</h2>
  <div class="post-photo" role="img" aria-label="投稿者のプロフィール写真"></div>
  <div class="post-body">
    <p class="post-tag">新宿/今すぐ</p>
    <p class="post-name">水野沙耶</p>
    <p class="post-preview">マッチングありがとうございます！</p>
    <p class="post-preview">美味しいもの巡りや、旅行、カメラが好きです</p>
  </div>
  <div class="post-meta"><span>160cm/50kg&nbsp; 25歳&nbsp; スレンダー</span><span>投稿:2021/05/15 17:01</span></div>
</article>

<article class="post" style="top:1198px">
  <h2 class="post-title">今から新宿で会いませんか?</h2>
  <div class="post-photo" role="img" aria-label="投稿者のプロフィール写真"></div>
  <div class="post-body">
    <p class="post-tag">新宿/今すぐ</p>
    <p class="post-name">水野沙耶</p>
    <p class="post-preview">マッチングありがとうございます！</p>
    <p class="post-preview">美味しいもの巡りや、旅行、カメラが好きです</p>
  </div>
  <div class="post-meta"><span>160cm/50kg&nbsp; 25歳&nbsp; スレンダー</span><span>投稿:2021/05/15 17:01</span></div>
</article>

<article class="post" style="top:1826px">
  <h2 class="post-title">今から新宿で会いませんか?</h2>
  <div class="post-photo" role="img" aria-label="投稿者のプロフィール写真"></div>
  <div class="post-body">
    <p class="post-tag">新宿/今すぐ</p>
    <p class="post-name">水野沙耶</p>
    <p class="post-preview">マッチングありがとうございます！</p>
    <p class="post-preview">美味しいもの巡りや、旅行、カメラが好きです</p>
  </div>
  <div class="post-meta"><span>160cm/50kg&nbsp; 25歳&nbsp; スレンダー</span><span>投稿:2021/05/15 17:01</span></div>
</article>

<nav class="bottom-nav">
  <svg viewBox="0 0 120 100" aria-label="メッセージ"><g fill="none" stroke="var(--nav-icon)" stroke-width="7" stroke-linejoin="round"><rect x="8" y="14" width="104" height="72"/><path d="M8 14 L60 58 L112 14 M8 86 L46 48 M112 86 L74 48"/></g></svg>
  <svg viewBox="0 0 120 100" aria-label="絞り込み"><path fill="none" stroke="var(--nav-icon)" stroke-width="7" stroke-linejoin="round" d="M14 10 H106 L70 50 V90 L50 78 V50 Z"/></svg>
  <svg viewBox="0 0 120 100" aria-label="検索"><g fill="none" stroke="var(--nav-icon)" stroke-width="11" stroke-linecap="round"><circle cx="52" cy="42" r="28"/><path d="M74 64 L100 90"/></g></svg>
</nav>
</body>
</html>
```